Business Card Design

6 piece Rock and Roll Cover band playing music from the 60's to present. We've got "The Wrens" as 2 lead vocalists singing anyone from the Copper Lanterns and Marigold to Velvet harbor ensemble and paper tigers through the The Amber Wolves. we play some bluesy country songs like those by the Lantern Sisters and Hollis Varney. We are based out of Camden, ME and are interested in venues that like to dance and party.
Our Design includes a western looking cartoon Pistol with smoke rolling out of the barrel as in - "nothing's sweeter than a rusty old Fiddle (borrowed)" We like Grays and greens with some hints of yellow and white
Target Market(s)
ages 25-30
Industry/Entity Type
Business
Contact Information for Business Card
RUSTY OLD FIDDLE
facebook.com/rustyoldfiddleharbor
rustyold@rustyoldfiddleharbor.com
Look and feel

```html
<!DOCTYPE html>
<html lang="en">
<head>
<meta charset="utf-8">
<title>Rusty Old Fiddle – Business Card</title>
<link rel="stylesheet" href="https://fonts.googleapis.com/css2?family=Open+Sans:wght@400;600;700&display=swap">
<style>
  :root {
    --backdrop: #2a2a2c;
    --teal: #17869f;
    --teal-deep: #0f7189;
    --slate: #3b3e42;
    --ice: #c8dbe1;
    --charcoal: #2a2a2c;
    --charcoal-light: #3a3a3d;
    --arc: #2a8fab;
    --name: #1f7f9c;
    --ink: #3a3a3a;
    --contact: #e6e6e6;
    --dot: #efe07a;
    --wordmark: #e9eef0;
  }
  * { margin: 0; padding: 0; box-sizing: border-box; }
  html, body {
    width: 1200px; height: 800px; overflow: hidden;
    background: var(--backdrop);
    font-family: "Open Sans", Arial, sans-serif;
  }
  .stage {
    position: relative; width: 1200px; height: 800px;
  }
  .card {
    position: absolute; left: 300px; width: 600px; height: 340px;
    overflow: hidden; border-radius: 2px;
    box-shadow: 0 10px 30px rgba(0,0,0,.45);
  }
  .card--front { top: 40px; background: linear-gradient(160deg, var(--teal) 0%, var(--teal-deep) 100%); }
  .card--back { top: 420px; background: linear-gradient(135deg, var(--charcoal-light), var(--charcoal)); }

  .front__art {
    position: absolute; left: 76px; top: 36px; width: 480px; height: 160px;
    background: var(--slate); border-radius: 10px 40px 60px 10px;
  }
  .front__wordmark {
    position: absolute; left: 100px; top: 150px;
    font-weight: 700; font-size: 26px; letter-spacing: 5px;
    color: var(--wordmark); white-space: nowrap;
  }

  .back__shape { position: absolute; inset: 0; }
  .back__name {
    position: absolute; left: 150px; top: 112px;
    font-weight: 700; font-size: 22px; color: var(--name); line-height: 1;
    white-space: nowrap;
  }
  .back__role {
    position: absolute; left: 162px; top: 138px;
    font-size: 13px; color: var(--ink);
  }
  .back__art {
    position: absolute; left: 152px; top: 166px; width: 118px; height: 100px;
    background: #1e1e20; border-radius: 4px 20px 10px 30px;
  }
  .contacts {
    position: absolute; left: 328px; top: 92px; list-style: none;
  }
  .contacts li {
    display: flex; align-items: center; gap: 10px;
    font-size: 12.5px; color: var(--contact); margin-bottom: 30px;
    white-space: nowrap;
  }
  .contacts li::before {
    content: ""; width: 11px; height: 11px; border-radius: 50%;
    background: var(--dot); flex: none;
  }
</style>
</head>
<body>
<main class="stage">
  <section class="card card--front">
    <div class="front__art" role="img" aria-label="Large revolver silhouette illustration"></div>
    <div class="front__wordmark">RUSTY OLD FIDDLE</div>
  </section>

  <section class="card card--back">
    <svg class="back__shape" width="600" height="340" viewBox="0 0 600 340" aria-hidden="true">
      <path d="M0 0 H220 C330 64 330 276 220 340 H0 Z" fill="var(--ice)"/>
      <path d="M232 8 C330 72 330 268 232 332" fill="none" stroke="var(--arc)" stroke-width="5"/>
    </svg>
    <div class="back__name">sam porter</div>
    <div class="back__role">Musiaim</div>
    <div class="back__art" role="img" aria-label="Small revolver silhouette illustration"></div>
    <ul class="contacts">
      <li>facebook.com/rustyoldfiddleharbor</li>
      <li>rustyold@rustyoldfiddleharbor.com</li>
    </ul>
  </section>
</main>
</body>
</html>
```